Tasman Curdworks Guild needs new business cards

We need new business cards designed and produced. We are likely to need other design work done for ads, flyers etc in future.

We would like to start with an initial business card.

The Tasman Curdworks Guild (TCG) is a membership-based not-for-profit organisation that looks after the interests of Australia's small to medium artisan cheesemakers, many of whom are also small-scale farmers. The design should be simple, using our logo, but also communicate our artisan cheese and small dairy farm focus.

The first card to be designed and produced is for me, Miriam Tolhurst. My details are:

Miriam Tolhurst
Secretary
Tasman Curdworks Guild (TCG)
http://www.curdworksguild.example
T +61452837190
E miriam.miriamtolhurst@mailbox.example

I have attached the TCG logo in jpg form. I have a higher resolution version available if needed.

Thank you!

Miriam

Miriam Tolhurst
Tasman Curdworks Guild
miriam.miriamtolhurst@mailbox.example
+61452837190

Sans Serif

• Logo (see attached file)

```html
<!DOCTYPE html>
<html lang="en">
<head>
<meta charset="utf-8">
<title>Tasman Curdworks Guild – Business Card</title>
<link rel="stylesheet" href="https://fonts.googleapis.com/css2?family=Crimson+Pro:wght@400;700&family=Open+Sans:wght@400&display=swap">
<style>
  :root {
    --backdrop: #1e1e1e;
    --card-white: #ffffff;
    --brown: #5c3a17;
    --cheese: #f9c76b;
    --ink: #555555;
    --rule: #a08a70;
  }
  * { margin: 0; padding: 0; box-sizing: border-box; }
  html, body {
    width: 1200px; height: 987px; overflow: hidden;
    background: var(--backdrop);
  }
  .canvas { position: relative; width: 1200px; height: 987px; }
  .card {
    position: absolute; left: 293px; width: 615px; height: 352px;
    border-radius: 16px; overflow: hidden;
  }
  .card--front { top: 130px; background: var(--card-white); }
  .card--back { top: 505px; background: var(--brown); }

  .brand { position: absolute; display: flex; align-items: center; }
  .brand__dot { border-radius: 50%; background: var(--cheese); flex: none; }
  .brand__name {
    font-family: "Crimson Pro", Georgia, serif; font-weight: 400;
    line-height: 1.05;
  }
  .card--front .brand { left: 41px; top: 42px; }
  .card--front .brand__dot { width: 70px; height: 70px; margin-right: 42px; }
  .card--front .brand__name { font-size: 26px; color: var(--brown); }

  .card--back .brand { left: 144px; top: 118px; }
  .card--back .brand__dot { width: 100px; height: 100px; margin-right: 34px; }
  .card--back .brand__name { font-size: 31px; color: var(--card-white); }

  .holder {
    position: absolute; right: 33px; top: 152px; text-align: right;
    font-family: "Crimson Pro", Georgia, serif;
  }
  .holder__name { font-size: 24px; font-weight: 700; color: var(--brown); line-height: 1.1; }
  .holder__role { font-size: 16px; color: var(--cheese); line-height: 1.1; }

  .divider {
    position: absolute; left: 59px; right: 33px; top: 212px; height: 1px;
    background: linear-gradient(to right, rgba(160,138,112,0), var(--rule) 40%, var(--brown));
  }
  .contact {
    position: absolute; left: 41px; top: 250px;
    font-family: "Crimson Pro", Georgia, serif; font-size: 17px;
    color: var(--ink); line-height: 24px;
  }
  .contact__label { font-weight: 700; color: var(--brown); }

  .footer-band { position: absolute; left: 0; top: 0; }
  .web {
    position: absolute; font-family: "Open Sans", Arial, sans-serif;
    color: var(--card-white);
  }
  .card--front .web { right: 25px; top: 323px; font-size: 14px; letter-spacing: 1.5px; }
  .card--back .web { left: 0; right: 0; top: 293px; text-align: center; font-size: 15px; letter-spacing: 4.5px; }
</style>
</head>
<body>
<div class="canvas">
  <section class="card card--front">
    <div class="brand">
      <span class="brand__dot"></span>
      <div class="brand__name">Tasman<br>Curdworks<br>Guild</div>
    </div>
    <div class="holder">
      <div class="holder__name">Miriam Tolhurst</div>
      <div class="holder__role">Secretary</div>
    </div>
    <div class="divider"></div>
    <div class="contact">
      <div><span class="contact__label">Phone:</span> +61452837190</div>
      <div>miriam.miriamtolhurst@mailbox.example</div>
    </div>
    <svg class="footer-band" width="615" height="352" viewBox="0 0 615 352" aria-hidden="true">
      <rect x="0" y="327" width="330" height="9" fill="var(--cheese)"/>
      <path d="M615 313 H345 Q322 313 314 325 Q305 338 282 338 H0 V352 H615 Z" fill="var(--brown)"/>
    </svg>
    <div class="web">www.curdworksguild.example</div>
  </section>

  <section class="card card--back">
    <div class="brand">
      <span class="brand__dot"></span>
      <div class="brand__name">Tasman<br>Curdworks<br>Guild</div>
    </div>
    <div class="web">www.curdworksguild.example</div>
  </section>
</div>
</body>
</html>
```